Lucid Haven - Need Stationary Design

We need a stationary pack for our new Care company based in the uk
Are corporate colours are Pink and purple
Please use attached logo
Target Market(s)
The Care Industry
Industry/Entity Type
It Company
Contact Information for Business Card
Moira Blythe
Director

```html
<!DOCTYPE html>
<html lang="en">
<head>
<meta charset="utf-8">
<title>Lucid Haven Business Card</title>
<link href="https://fonts.googleapis.com/css2?family=Arimo:wght@400;700&display=swap" rel="stylesheet">
<style>
  :root {
    --page: #e9e6ee;
    --white: #ffffff;
    --pink: #e0399e;
    --pink-light: #ee6fbd;
    --purple: #7a4aa3;
    --purple-dark: #5a3580;
    --lavender: #a37ccb;
    --lavender-soft: #d9c8ea;
    --ink-purple: #7b4da6;
  }
  * { margin: 0; padding: 0; box-sizing: border-box; }
  html, body { width: 1200px; height: 950px; overflow: hidden; }
  body {
    background: var(--page);
    font-family: "Arimo", Arial, sans-serif;
    position: relative;
  }
  .card {
    position: absolute;
    left: 220px;
    width: 760px;
    height: 434px;
    border-radius: 6px;
    overflow: hidden;
    box-shadow: 0 8px 24px rgba(60, 30, 90, 0.18);
  }
  .card-front { top: 30px; background: var(--white); }
  .card-back {
    top: 486px;
    background: linear-gradient(100deg, var(--purple) 0%, #8458ae 45%, var(--purple-dark) 100%);
  }
  .card-art { position: absolute; inset: 0; width: 100%; height: 100%; }

  .brand {
    position: absolute;
    left: 60px;
    top: 110px;
    width: 320px;
    display: flex;
    flex-direction: column;
    align-items: center;
    gap: 16px;
  }
  .brand-dot {
    width: 56px; height: 56px; border-radius: 50%;
    background: var(--pink);
  }
  .brand-name {
    font-size: 40px;
    font-weight: 400;
    color: var(--ink-purple);
    letter-spacing: 0.5px;
    white-space: nowrap;
  }

  .contact {
    position: absolute;
    right: 44px;
    top: 100px;
    text-align: right;
    color: var(--white);
  }
  .contact-name { font-size: 28px; font-weight: 700; letter-spacing: 1px; }
  .contact-title { font-size: 18px; letter-spacing: 1.5px; margin-top: 2px; }
  .contact-address { font-size: 18px; line-height: 26px; margin-top: 30px; }
  .contact-lines { list-style: none; margin-top: 12px; }
  .contact-lines li {
    font-size: 18px;
    line-height: 27px;
    display: flex;
    justify-content: flex-end;
    align-items: center;
    gap: 10px;
    white-space: nowrap;
  }
  .contact-lines svg { width: 16px; height: 16px; fill: var(--white); flex: none; }

  .back-brand {
    position: absolute;
    inset: 0;
    display: flex;
    flex-direction: column;
    align-items: center;
    justify-content: center;
    gap: 18px;
  }
  .back-brand .brand-dot { width: 64px; height: 64px; background: var(--lavender-soft); }
  .back-brand .brand-name { font-size: 46px; color: var(--lavender-soft); }
</style>
</head>
<body>

<section class="card card-front">
  <svg class="card-art" viewBox="0 0 760 434" preserveAspectRatio="none" aria-hidden="true">
    <defs>
      <linearGradient id="pinkPanel" x1="0" y1="0" x2="1" y2="1">
        <stop offset="0" stop-color="#ee6fbd"/>
        <stop offset="1" stop-color="#d92f93"/>
      </linearGradient>
    </defs>
    <path d="M440 0 C400 200 330 370 150 434 L760 434 L760 0 Z" fill="url(#pinkPanel)"/>
    <path d="M440 0 C400 200 330 370 150 434 L215 434 C360 372 430 230 530 80 C545 58 560 40 575 0 Z" fill="#a37ccb"/>
    <path d="M478 0 C450 170 390 330 250 434 L215 434 C360 372 430 230 530 80 C545 58 560 40 575 0 Z" fill="#7a4aa3" opacity="0.55"/>
    <path d="M500 0 C470 180 400 340 270 434 L300 434 C440 330 510 170 530 0 Z" fill="url(#pinkPanel)"/>
  </svg>

  <div class="brand">
    <span class="brand-dot"></span>
    <span class="brand-name">Lucid Haven</span>
  </div>

  <div class="contact">
    <p class="contact-name">MOIRA BLYTHE</p>
    <p class="contact-title">DIRECTOR</p>
    <p class="contact-address">14 Marlow Court<br>Ashford, Kent TN23 1AB</p>
    <ul class="contact-lines">
      <li>01233 416 408
        <svg viewBox="0 0 16 16"><path d="M3 2h3l1.5 3.5-2 1.2a8 8 0 0 0 3.8 3.8l1.2-2L14 10v3a1 1 0 0 1-1 1A11 11 0 0 1 2 3a1 1 0 0 1 1-1z"/></svg></li>
      <li>07862 140 359
        <svg viewBox="0 0 16 16"><rect x="4" y="1" width="8" height="14" rx="1.5"/><rect x="5.5" y="3" width="5" height="8" fill="#e0399e"/></svg></li>
      <li>01233 603 822
        <svg viewBox="0 0 16 16"><rect x="4" y="1" width="8" height="5"/><rect x="1" y="6" width="14" height="6" rx="1"/><rect x="4" y="10" width="8" height="5" fill="#fff" stroke="#e0399e"/></svg></li>
      <li>moira@lucidhaven.co.uk
        <svg viewBox="0 0 16 16"><rect x="1" y="3" width="14" height="10" rx="1"/><path d="M1.5 3.5 8 9l6.5-5.5" fill="none" stroke="#e0399e" stroke-width="1.3"/></svg></li>
      <li>www.lucidhaven.co.uk
        <svg viewBox="0 0 16 16"><circle cx="8" cy="8" r="7"/><path d="M7 4l4 4-4 4" fill="none" stroke="#e0399e" stroke-width="1.6"/></svg></li>
    </ul>
  </div>
</section>

<section class="card card-back">
  <div class="back-brand">
    <span class="brand-dot"></span>
    <span class="brand-name">Lucid Haven</span>
  </div>
</section>

</body>
</html>
```